Quiet Harbour A Recovery-Centred Pathway

I am giving a presentation through an interpreter I want to make this design work visually for a high profile client from Saudi Arabia where i will be discussing mental health and wellbeing of workers supporting protecting workers in critical occupations in challenging countries key points need to be visual and polished and professional video animation will work with my logo

I have now updated the slide deck for your design

Target Market(s)

A delegation of important medical people from the KSA

Industry/Entity Type

medical professionals

Requirements
Must have
• translatable into Arabic good graphics and visuals as it will be presented through and interpreter.
Nice to have
• video https://www.vidmarlo.com/feed/downloads
Should not have
• translatable into Arabic

```html
<!DOCTYPE html>
<html lang="en">
<head>
<meta charset="utf-8">
<title>Quiet Harbour – Decompression Sessions Deck</title>
<link rel="stylesheet" href="https://fonts.googleapis.com/css2?family=Poppins:wght@300;400;500;600;700&family=Yellowtail&display=swap">
<style>
:root{
  --board:#a3c7bd;
  --slide-edge:#b9d7cf;
  --slide-light:#f2f7f5;
  --card:#9fc7bc;
  --ink:#1f2322;
  --ink-soft:#4f5a57;
  --card-text:#eef6f3;
  --photo-a:#6f8f8a;
  --photo-b:#a9b9b4;
  --white:#ffffff;
}
*{margin:0;padding:0;box-sizing:border-box}
html,body{width:1200px;height:820px;overflow:hidden;background:var(--board)}
body{position:relative;font-family:"Poppins",sans-serif;color:var(--ink)}
.slide{position:absolute;width:329px;height:185px;overflow:hidden;
  background:radial-gradient(ellipse at 50% 55%,var(--slide-light) 0%,#d9eae5 45%,var(--slide-edge) 100%);
  box-shadow:0 6px 14px rgba(40,80,70,.22)}
.slide--cover{background:var(--card)}
.abs{position:absolute}
.slide-title{position:absolute;left:0;right:0;text-align:center;font-family:"Yellowtail",cursive;font-size:19px;line-height:1;color:var(--ink)}
.title-bar{position:absolute;left:50%;width:18px;height:1.5px;margin-left:-9px;background:var(--ink)}
.footer{position:absolute;left:0;right:0;bottom:0;height:11px;background:var(--card);display:flex;align-items:center;font-size:3.4px;color:var(--white);padding-left:7px}
.footer span{display:flex;align-items:center;gap:2px}
.footer .sep{margin:0 10px}
.footer .foot-brand{position:absolute;right:0;top:0;bottom:0;width:32px;border-left:1px solid rgba(255,255,255,.7);display:flex;align-items:center;justify-content:center;font-weight:300;font-size:4px}
.card{position:absolute;background:var(--card);box-shadow:0 2px 5px rgba(40,80,70,.25);text-align:center;padding:4px 4px}
.card h3{font-size:4.3px;font-weight:700;line-height:1.2;color:var(--ink)}
.card p{font-size:3.4px;line-height:1.4;color:var(--card-text);margin-top:3px}
.photo{position:absolute;background:linear-gradient(135deg,var(--photo-a),var(--photo-b));box-shadow:0 2px 5px rgba(40,80,70,.25)}
.brand-name{font-weight:300;color:var(--white);white-space:nowrap}
.brand-tag{font-weight:400;color:var(--white);white-space:nowrap;text-transform:uppercase}
.timeline{position:absolute;height:.6px;background:#7a8a86}
.dot{position:absolute;width:3.5px;height:3.5px;border-radius:50%;background:var(--ink);margin:-1.5px 0 0 -1.75px}
.contact-row{position:absolute;left:24px;display:flex;align-items:flex-start;gap:5px}
.contact-icon{width:10px;height:10px;border-radius:50%;background:var(--card);display:flex;align-items:center;justify-content:center;flex:none}
.contact-row small{display:block;font-size:3px;color:var(--ink-soft)}
.contact-row strong{display:block;font-size:7px;font-weight:600;line-height:1.2}
</style>
</head>
<body>

<!-- Cover -->
<section class="slide slide--cover" style="left:57px;top:81px">
  <div class="abs" style="left:0;right:0;top:62px;text-align:center">
    <div class="brand-name" style="font-size:13px">Elmsley Reed</div>
    <div class="brand-tag" style="font-size:2.6px;letter-spacing:1.3px;margin-top:2px">Cognitive Behavioural Services</div>
    <div style="font-size:7.5px;letter-spacing:2px;color:var(--white);margin-top:16px;line-height:1.65">DECOMPRESSION<br>SESSIONS</div>
    <div style="width:44px;height:8px;background:#6d5aa0;border-radius:2px;margin:3px auto 0"></div>
    <div style="font-size:2.4px;color:var(--white);line-height:1.6;margin-top:3px">LEAD CLINICIAN MSC, BSC (HONS), REGISTERED THERAPIST<br>ACCREDITED PRACTITIONER<br>EXPERT WITNESS</div>
  </div>
</section>

<!-- Title -->
<section class="slide" style="left:435px;top:81px">
  <h1 class="slide-title" style="top:38px;font-size:19px;line-height:1.12">Supporting Critical<br>Workers in Their<br>Traumatic Work</h1>
  <div class="title-bar" style="top:106px"></div>
  <p class="abs" style="left:0;right:0;top:114px;text-align:center;font-size:8px;font-weight:600;color:var(--ink-soft);line-height:1.25">Providing a roadmap of care and<br>support for frontline professionals</p>
  <footer class="footer"><span>✉ hello@elmsleyreedcbt.co.uk</span><span class="sep">|</span><span>☏ 0700.555.0142</span><div class="foot-brand">Elmsley Reed</div></footer>
</section>

<!-- On-the-Job Support -->
<section class="slide" style="left:813px;top:81px">
  <h2 class="slide-title" style="top:8px">On-the-Job Support</h2>
  <div class="title-bar" style="top:35px"></div>
  <div class="card" style="left:20px;top:51px;width:65px;height:92px">
    <svg width="18" height="18" viewBox="0 0 24 24" fill="none" stroke="#1f2322" stroke-width="1.2" style="margin-top:10px"><circle cx="14" cy="8" r="4"/><circle cx="14" cy="8" r="1.5"/><path d="M3 15h4l4 2h5a1.5 1.5 0 0 1 0 3H9M3 21h4l3-1"/></svg>
    <h3 style="margin-top:4px">Peer Support<br>Systems</h3>
    <p>Peer support and team check-ins foster community and reduce isolation among critical workers.</p>
  </div>
  <div class="card" style="left:96px;top:51px;width:65px;height:92px">
    <svg width="18" height="18" viewBox="0 0 24 24" fill="none" stroke="#1f2322" stroke-width="1.2" style="margin-top:10px"><rect x="3" y="7" width="18" height="13" rx="1.5"/><path d="M9 7V4h6v3M12 10v7M8.5 13.5h7"/></svg>
    <h3 style="margin-top:4px">Group<br>Psychological First<br>Aid</h3>
    <p>GPFA provides structured support focusing on safety, calmness, and connectedness to manage acute stress.</p>
  </div>
  <div class="card" style="left:171px;top:51px;width:65px;height:92px">
    <svg width="18" height="18" viewBox="0 0 24 24" fill="none" stroke="#1f2322" stroke-width="1.2" style="margin-top:10px"><circle cx="12" cy="7" r="4"/><path d="M3 12l9 2 9-2v9l-9 2-9-2zM12 14v9"/></svg>
    <h3 style="margin-top:4px">Confidential<br>Mental Health<br>Resources</h3>
    <p>Access to confidential, culturally sensitive mental health resources helps workers seek help without stigma.</p>
  </div>
  <div class="card" style="left:246px;top:51px;width:65px;height:92px">
    <svg width="18" height="18" viewBox="0 0 24 24" fill="none" stroke="#1f2322" stroke-width="1.2" style="margin-top:10px"><circle cx="12" cy="12" r="9"/><circle cx="12" cy="12" r="5"/><path d="M9.5 12l2 2 3.5-4"/></svg>
    <h3 style="margin-top:4px">Creating<br>Psychologically<br>Safe Environments</h3>
    <p>Integrating support mechanisms daily promotes resilience, recovery, and sustained performance in teams.</p>
  </div>
  <footer class="footer"><span>✉ hello@elmsleyreedcbt.co.uk</span><span class="sep">|</span><span>☏ 0700.555.0142</span><div class="foot-brand">Elmsley Reed</div></footer>
</section>

<!-- Organisational Policies -->
<section class="slide" style="left:57px;top:317px">
  <h2 class="slide-title" style="top:8px">Organisational Policies</h2>
  <div class="title-bar" style="top:35px"></div>
  <div class="photo" role="img" aria-label="Photo of colleagues in a team discussion" style="left:8px;top:48px;width:95px;height:59px"></div>
  <div class="photo" role="img" aria-label="Photo of a manager training session around a table" style="left:116px;top:48px;width:95px;height:59px"></div>
  <div class="photo" role="img" aria-label="Photo of an open-plan office with staff at desks" style="left:224px;top:48px;width:95px;height:59px"></div>
  <div class="card" style="left:16px;top:96px;width:78px;height:58px"><h3>Mental Health<br>Integration</h3><p>Integrating mental health into risk management frameworks ensures psychological wellbeing is prioritised alongside physical safety.</p></div>
  <div class="card" style="left:124px;top:96px;width:78px;height:58px"><h3>Manager<br>Training</h3><p>Training managers to recognise trauma and stress enables proactive support for staff mental health.</p></div>
  <div class="card" style="left:232px;top:96px;width:78px;height:58px"><h3>Policy Communication<br>and Culture</h3><p>Clear communication and consistent application of policies build trust and encourage help-seeking culture.</p></div>
  <footer class="footer"><span>✉ hello@elmsleyreedcbt.co.uk</span><span class="sep">|</span><span>☏ 0700.555.0142</span><div class="foot-brand">Elmsley Reed</div></footer>
</section>

<!-- Post-Deployment Care -->
<section class="slide" style="left:435px;top:317px">
  <h2 class="slide-title" style="top:8px">Post-Deployment Care</h2>
  <div class="title-bar" style="top:35px"></div>
  <div class="timeline" style="left:79px;width:160px;top:105px"></div>
  <div class="dot" style="left:79px;top:105px"></div><div class="dot" style="left:159px;top:105px"></div><div class="dot" style="left:239px;top:105px"></div>
  <div class="card" style="left:48px;top:48px;width:62px;height:46px"><h3>Structured Debriefing<br>Sessions</h3><p>These sessions offer a safe space for reflection and emotional processing, led by trained staff.</p></div>
  <div class="photo" role="img" aria-label="Photo of medical staff in conversation" style="left:128px;top:48px;width:62px;height:46px"></div>
  <div class="card" style="left:207px;top:48px;width:62px;height:46px"><h3>Follow-up<br>therapy</h3><p>Ongoing therapy ensures delayed trauma responses are addressed and support continues over time.</p></div>
  <div class="photo" role="img" aria-label="Photo of a group support session" style="left:48px;top:112px;width:62px;height:47px"></div>
  <div class="card" style="left:128px;top:112px;width:62px;height:47px"><h3>Support for Reverse<br>Culture Shock</h3><p>Organisations provide resources and guidance to help staff reintegrate smoothly after deployment challenges.</p></div>
  <div class="photo" role="img" aria-label="Photo of a clinician with a family" style="left:207px;top:112px;width:62px;height:47px"></div>
  <footer class="footer"><span>✉ hello@elmsleyreedcbt.co.uk</span><span class="sep">|</span><span>☏ 0700.555.0142</span><div class="foot-brand">Elmsley Reed</div></footer>
</section>

<!-- Culture Change -->
<section class="slide" style="left:813px;top:317px">
  <h2 class="slide-title" style="top:8px">Culture Change</h2>
  <div class="title-bar" style="top:35px"></div>
  <div class="timeline" style="left:47px;width:243px;top:105px"></div>
  <div class="dot" style="left:47px;top:105px"></div><div class="dot" style="left:127px;top:105px"></div><div class="dot" style="left:207px;top:105px"></div><div class="dot" style="left:290px;top:105px"></div>
  <div class="card" style="left:15px;top:48px;width:63px;height:46px"><h3>Normalising<br>Help-Seeking</h3><p>Reducing stigma and encouraging open conversations make seeking help a normal behaviour.</p></div>
  <div class="card" style="left:176px;top:48px;width:63px;height:46px"><h3>Localising Mental<br>Health Support</h3><p>Adapting interventions to local contexts and cultures ensures access for staff and volunteers.</p></div>
  <div class="card" style="left:96px;top:112px;width:63px;height:47px"><h3>Leadership Modeling<br>Vulnerability</h3><p>Leaders showing support and vulnerability foster a place where asking for help is a strength.</p></div>
  <div class="card" style="left:259px;top:112px;width:63px;height:47px"><h3>Promoting Inclusivity<br>and Equity</h3><p>Inclusive mental health care builds team trust and cohesion, embedding support as shared duty.</p></div>
  <footer class="footer"><span>✉ hello@elmsleyreedcbt.co.uk</span><span class="sep">|</span><span>☏ 0700.555.0142</span><div class="foot-brand">Elmsley Reed</div></footer>
</section>

<!-- Pre-Deployment Preparation -->
<section class="slide" style="left:57px;top:553px">
  <h2 class="slide-title" style="top:8px">Pre-Deployment Preparation</h2>
  <div class="title-bar" style="top:30px"></div>
  <div class="photo" role="img" aria-label="Photo of a rehabilitation training session" style="left:7px;top:39px;width:76px;height:52px"></div>
  <div class="photo" role="img" aria-label="Photo of a screening interview" style="left:86px;top:39px;width:76px;height:52px"></div>
  <div class="photo" role="img" aria-label="Photo of staff briefing in a hallway" style="left:165px;top:39px;width:76px;height:52px"></div>
  <div class="photo" role="img" aria-label="Photo of a team reviewing data together" style="left:246px;top:39px;width:76px;height:52px"></div>
  <div class="card" style="left:13px;top:90px;width:62px;height:72px"><h3>Comprehensive<br>Trauma Training</h3><p>Training helps workers understand how trauma shows, recognise its signs in themselves and others, and adopt approaches that reduce re-traumatisation at work.</p></div>
  <div class="card" style="left:93px;top:90px;width:62px;height:72px"><h3>Psychological<br>Screening</h3><p>Screening assesses existing mental health conditions, stress, or burnout before deployment to potentially traumatic settings, using tools such as questionnaires.</p></div>
  <div class="card" style="left:172px;top:90px;width:62px;height:72px"><h3>Expectation<br>Management</h3><p>Clear communication prepares workers for moral dilemmas, cultural challenges, and resource limits.</p></div>
  <div class="card" style="left:253px;top:90px;width:62px;height:72px"><h3>Building Resilience<br>Foundation</h3><p>Combined preparation enhances mental wellbeing and resilience before deployment.</p></div>
  <footer class="footer"><span>✉ hello@elmsleyreedcbt.co.uk</span><span class="sep">|</span><span>☏ 0700.555.0142</span><div class="foot-brand">Elmsley Reed</div></footer>
</section>

<!-- Contact -->
<section class="slide" style="left:428px;top:553px">
  <h2 class="slide-title" style="left:19px;right:auto;top:18px;text-align:left">Contact Us</h2>
  <div class="abs" style="left:19px;top:46px;width:18px;height:1.5px;background:var(--ink)"></div>
  <div class="abs" style="left:161px;top:0;width:168px;height:60px;background:var(--card);text-align:center;padding-top:20px">
    <div class="brand-name" style="font-size:15px">Elmsley Reed</div>
    <div class="brand-tag" style="font-size:3.4px;letter-spacing:1.5px;margin-top:3px">Cognitive Behavioural Services</div>
  </div>
  <div class="contact-row" style="top:66px"><div class="contact-icon"><svg width="5" height="5" viewBox="0 0 24 24" fill="#1f2322"><path d="M6.6 10.8a15 15 0 0 0 6.6 6.6l2.2-2.2a1 1 0 0 1 1-.25 11 11 0 0 0 3.6.6 1 1 0 0 1 1 1V20a1 1 0 0 1-1 1A17 17 0 0 1 3 4a1 1 0 0 1 1-1h3.5a1 1 0 0 1 1 1 11 11 0 0 0 .6 3.6 1 1 0 0 1-.25 1z"/></svg></div><div><small>Call Us</small><strong>0700.555.0142</strong></div></div>
  <div class="contact-row" style="top:93px"><div class="contact-icon"><svg width="5" height="5" viewBox="0 0 24 24" fill="none" stroke="#1f2322" stroke-width="2.5"><rect x="3" y="5" width="18" height="14"/><path d="M3 6l9 7 9-7"/></svg></div><div><small>Email Us</small><strong>hello@elmsleyreedcbt.co.uk</strong></div></div>
  <div class="contact-row" style="top:120px"><div class="contact-icon"><svg width="5" height="5" viewBox="0 0 24 24" fill="#1f2322"><path d="M12 2a7 7 0 0 0-7 7c0 5 7 13 7 13s7-8 7-13a7 7 0 0 0-7-7zm0 9.5a2.5 2.5 0 1 1 0-5 2.5 2.5 0 0 1 0 5z"/></svg></div><div><small>Address</small><strong>18 Harbour Lane,<br>Brightwell,<br>40210</strong></div></div>
  <div class="abs" role="img" aria-label="Location map of the practice" style="left:184px;top:72px;width:133px;height:83px;border-radius:4px;background:linear-gradient(135deg,#dfeee4,#c9e4d3 60%,#e4eee9)"></div>
  <footer class="footer"><span>✉ hello@elmsleyreedcbt.co.uk</span><span class="sep">|</span><span>☏ 0700.555.0142</span></footer>
</section>

<!-- Brand sign-off -->
<div class="abs" style="left:850px;top:620px;width:260px;text-align:center">
  <div class="brand-name" style="font-size:40px;line-height:1">Elmsley Reed</div>
  <div class="brand-tag" style="font-size:8px;letter-spacing:3.4px;margin-top:8px">Cognitive Behavioural Services</div>
</div>

</body>
</html>
```